Home and body fragrance business needs a candle box design

We need a box design for our new line of luxury candles. Our products are tropical island inspired. In addition to the box, a matching label for the candle jar is required. Our logo, candle jar and lid are attached. We will be using an autolock box. Box template and sample photo are attached. The design should communicate reconnecting, reviving and relaxing at luxury island retreat.

Box Dimension = L= 3 inches W=3 inches H=3.725 inches

Box Front Text = "pure soy wax candle"; "Velmarine"(aroma name); "breath relax find you"(tagline)

Box Other Text = "HAND POURED. EACH CANDLE IS CLEAN BURNING, WITH A PURE COTTON WICK AND IS INFUSED WITH A HINT OF THE FINEST FRAGRANCE OF PARADISE"

Box Bottom Text = . Estimated burn time 75 hours. Net wt 370 g.

Jar label text = logo, and aroma name
Updates

Reason: I have increased the design budget in an effort to attack more design submissions.

Target Market(s)

Women 25 - 55

Industry/Entity Type

Business

Font styles to use
Serif
Script

Colors

Designer to choose colors to be used in the design.

Requirements
Must have
• Gold. Colours reminiscent of an Elegant LUXURY tropical island vacation. These candles will retail for $45 each, so an upscale design is essential.
Nice to have
• Designs that I like are: www.brindelmaroquest.com ; vorsanel.com; hapsilverdune.com;
Should not have
• Styles reminiscent of wasting away in tobrentwaldhay

```html
<!DOCTYPE html>
<html lang="en">
<head>
<meta charset="utf-8">
<title>Isle Marenca – Velmarine Candle Label</title>
<link rel="stylesheet" href="https://fonts.googleapis.com/css2?family=Cinzel:wght@400;500;600;700&display=swap">
<style>
  :root {
    --sand-gold: #9a7f5a;
    --label-gold: #9c7f5c;
    --deep-teal: #0b3a3a;
    --ink-teal: #0f3b39;
    --leaf-olive: #8c8a5c;
    --leaf-sage: #a9a77a;
    --leaf-bark: #5a4a2c;
    --card-white: #ffffff;
  }
  * { margin: 0; padding: 0; box-sizing: border-box; }
  html, body { width: 1200px; height: 820px; overflow: hidden; }
  body { background: var(--sand-gold); font-family: "Cinzel", serif; }

  .canvas { position: relative; width: 1200px; height: 820px; background: var(--sand-gold); }

  .foliage-panel {
    position: absolute; left: 225px; top: 103px; width: 817px; height: 599px;
    background:
      radial-gradient(ellipse 180px 120px at 8% 12%, rgba(169,167,122,.75), transparent 70%),
      radial-gradient(ellipse 200px 140px at 30% 8%, rgba(140,138,92,.7), transparent 70%),
      radial-gradient(ellipse 160px 220px at 6% 55%, rgba(90,74,44,.7), transparent 70%),
      radial-gradient(ellipse 170px 220px at 10% 88%, rgba(169,167,122,.7), transparent 70%),
      radial-gradient(ellipse 200px 140px at 88% 10%, rgba(140,138,92,.7), transparent 70%),
      radial-gradient(ellipse 150px 240px at 94% 45%, rgba(169,167,122,.6), transparent 70%),
      radial-gradient(ellipse 180px 120px at 90% 88%, rgba(90,74,44,.6), transparent 70%),
      radial-gradient(ellipse 220px 100px at 55% 95%, rgba(140,138,92,.65), transparent 70%),
      var(--deep-teal);
  }

  .label-frame {
    position: absolute; left: 344px; top: 204px; width: 551px; height: 408px;
    background: var(--sand-gold);
  }

  .label-card {
    position: absolute; left: 364px; top: 225px; width: 513px; height: 363px;
    background: var(--card-white); border-radius: 6px;
  }

  .label-text { position: absolute; left: 0; width: 1200px; text-align: center; line-height: 1; }
  .brand-name { top: 286px; left: 22px; font-size: 47px; font-weight: 400; color: var(--label-gold); letter-spacing: 1px; }
  .product-type { top: 348px; left: 22px; font-size: 21px; font-weight: 600; color: var(--ink-teal); letter-spacing: 1px; }
  .aroma-name { top: 398px; left: 12px; font-size: 44px; font-weight: 600; color: var(--label-gold); letter-spacing: 1px; }
  .tagline { top: 466px; left: 28px; font-size: 27px; font-weight: 600; color: var(--ink-teal); letter-spacing: 1px; }
  .tagline-rule {
    position: absolute; left: 418px; top: 499px; width: 419px; height: 4px; background: var(--label-gold);
  }
  .burn-time { top: 530px; left: 22px; font-size: 19px; font-weight: 600; color: var(--ink-teal); }
  .net-weight { top: 557px; left: 22px; font-size: 19px; font-weight: 600; color: var(--ink-teal); }
</style>
</head>
<body>
  <main class="canvas">
    <div class="foliage-panel" role="img" aria-label="Illustrated tropical banana and palm leaves in olive, sage and brown on a deep teal ground"></div>
    <div class="label-frame"></div>
    <div class="label-card"></div>

    <h1 class="label-text brand-name">Isle Marenca</h1>
    <p class="label-text product-type">PURE SOY WAX CANDLE</p>
    <h2 class="label-text aroma-name">Velmarine</h2>
    <p class="label-text tagline">BREATH RELAX FIND YOU</p>
    <div class="tagline-rule"></div>
    <p class="label-text burn-time">Estimated burn time 75 hours</p>
    <p class="label-text net-weight">Net wt 370 g</p>
  </main>
</body>
</html>
```